TONVALE - A modern gin bottle label

Design of a bottle label in a modern fresh design. The name of the gin is "TONVALE Phantom Batch K7". Please take a look at the tonvale.de website. on the main page of tonvale.de you can breathe the design direction here: 1) the taste of the gin should be composed of 10 botanicals ... an important scent note. ) a distinctive flavor is spicy and fresh 3.) The filling volume is 0.5 liters 4.) the alcohol content is 43% vol. 5.) the variety is called "dry gin" 6.) tonvale stands for "energy" and "love"

Target Market(s)

Alcohol consumer

Colors

Designer to choose colors to be used in the design.

Requirements
Must have
• the tonvale corporate logo must be included, the name of the gin is "TONVALE Phantom Batch K7"
Nice to have
• Please use the bottles template in the appendix. (The Black Bottles) they can use the saying "DESTILLED & BOTTLED BY OLD MARINER" in small letters

```html
<!DOCTYPE html>
<html lang="en">
<head>
<meta charset="utf-8">
<title>TONVALE Phantom Batch K7 – Dry Gin Label</title>
<link rel="stylesheet" href="https://fonts.googleapis.com/css2?family=Exo+2:wght@400;500;600;700&display=swap">
<style>
  :root {
    --page: #ffffff;
    --label: #000000;
    --white: #ffffff;
    --orange-light: #f7931e;
    --orange-deep: #f15a24;
    --green: #2db52d;
    --bloom-a: #f6a21a;
    --bloom-b: #e8541c;
    --bloom-c: #3aa935;
  }
  * { margin: 0; padding: 0; box-sizing: border-box; }
  html, body {
    width: 1200px;
    height: 1200px;
    overflow: hidden;
    background: var(--page);
  }
  .label {
    position: absolute;
    left: 280px;
    top: 60px;
    width: 640px;
    height: 1080px;
    background: var(--label);
    font-family: "Exo 2", sans-serif;
    color: var(--white);
  }
  .brand {
    position: absolute;
    top: 110px;
    left: 0;
    width: 100%;
    text-align: center;
  }
  .brand-dot {
    display: block;
    width: 44px;
    height: 44px;
    margin: 0 auto 22px;
    border-radius: 50%;
    background: var(--orange-deep);
  }
  .brand-name {
    font-size: 66px;
    font-weight: 700;
    letter-spacing: 12px;
    padding-left: 12px;
    line-height: 1;
    color: var(--white);
  }
  .bloom-art {
    position: absolute;
    left: 74px;
    top: 444px;
    width: 163px;
    height: 192px;
  }
  .edition {
    position: absolute;
    left: 247px;
    top: 440px;
    line-height: 1;
  }
  .edition-line {
    display: block;
    font-weight: 500;
    letter-spacing: -1px;
  }
  .edition-name { font-size: 62px; }
  .edition-batch { font-size: 56px; margin-top: 2px; }
  .edition-variety {
    font-size: 66px;
    margin-top: 4px;
    background: linear-gradient(90deg, var(--orange-light), var(--orange-deep));
    -webkit-background-clip: text;
    background-clip: text;
    color: transparent;
  }
  .specs {
    position: absolute;
    left: 81px;
    right: 83px;
    top: 820px;
  }
  .specs-row {
    display: flex;
    justify-content: space-between;
    font-size: 30px;
    font-weight: 500;
    letter-spacing: 2px;
  }
  .producer {
    margin-top: 10px;
    font-size: 22px;
    font-weight: 500;
    color: var(--green);
    white-space: nowrap;
    letter-spacing: -0.3px;
  }
</style>
</head>
<body>
  <main class="label">
    <header class="brand">
      <span class="brand-dot"></span>
      <div class="brand-name">TONVALE</div>
    </header>

    <svg class="bloom-art" role="img" aria-label="Floral sugar-skull illustration in orange, yellow and green" viewBox="0 0 163 192">
      <defs>
        <linearGradient id="bloomFill" x1="0" y1="0" x2="1" y2="1">
          <stop offset="0" stop-color="var(--bloom-a)"/>
          <stop offset="0.6" stop-color="var(--bloom-b)"/>
          <stop offset="1" stop-color="var(--bloom-c)"/>
        </linearGradient>
      </defs>
      <rect width="163" height="192" rx="18" fill="url(#bloomFill)" opacity="0.85"/>
    </svg>

    <section class="edition">
      <span class="edition-line edition-name">PHANTOM</span>
      <span class="edition-line edition-batch">BATCH K7</span>
      <span class="edition-line edition-variety">DRY GIN</span>
    </section>

    <footer class="specs">
      <div class="specs-row">
        <span class="volume">0.5 liters</span>
        <span class="strength">43% alc/vol</span>
      </div>
      <p class="producer">DESTILLED &amp; BOTTLED BY OLD MARINER</p>
    </footer>
  </main>
</body>
</html>
```